Horticulture Consulting Company Premium Card

We are looking for new design for a premium business card.
Our cards will be printed on glossy and embossed premium card stock.

Target Market(s)

Horticulture business owners needing our consulting services

Contact Information for Business Card

Marcus Trell
(555) 304-2698
Marc@verdanilo.com

Requirements
Must have
• Company Logo and Contact information.
• Some additional work to add interest to the card
Should not have
• Red or Yellow

```html
<!DOCTYPE html>
<html lang="en">
<head>
<meta charset="utf-8">
<title>Verdanilo – Business Card</title>
<link rel="stylesheet" href="https://fonts.googleapis.com/css2?family=Montserrat:wght@700;800&family=Nunito:wght@600;700&display=swap">
<style>
  :root {
    --page: #ededed;
    --card-white: #ffffff;
    --brand-blue: #1a70b8;
    --brand-green: #3db54a;
    --ink-grey: #4a4a4a;
  }
  * { box-sizing: border-box; margin: 0; padding: 0; }
  html, body {
    width: 1200px; height: 1200px; overflow: hidden;
    background: var(--page);
    font-family: "Nunito", sans-serif;
  }
  .card {
    position: absolute; left: 250px; width: 700px; height: 378px;
  }
  .card--front { top: 163px; background: var(--card-white); }
  .card--back { top: 644px; background: var(--brand-green); }

  .brand {
    position: absolute; left: 35px; top: 0; width: 300px; height: 378px;
    display: flex; flex-direction: column; align-items: center; justify-content: center; gap: 14px;
  }
  .brand__lockup { display: flex; align-items: center; gap: 12px; }
  .brand__dot { width: 26px; height: 26px; border-radius: 50%; background: var(--brand-green); }
  .brand__name {
    font-family: "Montserrat", sans-serif; font-weight: 800;
    font-size: 46px; color: var(--brand-blue); letter-spacing: -1px;
  }
  .brand__tagline {
    font-size: 12.5px; font-weight: 700; color: var(--ink-grey);
    letter-spacing: 0.4px; text-transform: uppercase;
  }

  .divider {
    position: absolute; left: 368px; top: 66px; width: 3px; height: 244px;
    background: var(--brand-green);
  }

  .contact { position: absolute; left: 388px; top: 62px; color: var(--brand-blue); }
  .contact__name {
    font-family: "Montserrat", sans-serif; font-weight: 800;
    font-size: 41px; line-height: 1; letter-spacing: -1.5px;
  }
  .contact__role { color: var(--brand-green); font-weight: 700; font-size: 16px; margin-top: 4px; }
  .contact__list { list-style: none; margin-top: 36px; display: flex; flex-direction: column; gap: 11px; }
  .contact__item { display: flex; align-items: center; gap: 6px; font-size: 16px; font-weight: 700; }
  .contact__icon { width: 28px; height: 22px; flex: none; }
  .contact__address { margin-top: 30px; font-size: 16px; font-weight: 700; line-height: 1.3; }

  .back-brand {
    position: absolute; inset: 0;
    display: flex; align-items: center; justify-content: center; gap: 18px;
  }
  .back-brand__dot { width: 44px; height: 44px; border-radius: 50%; background: var(--card-white); }
  .back-brand__name {
    font-family: "Montserrat", sans-serif; font-weight: 800;
    font-size: 72px; color: var(--card-white); letter-spacing: -2px;
  }
</style>
</head>
<body>
  <section class="card card--front">
    <div class="brand">
      <div class="brand__lockup">
        <span class="brand__dot"></span>
        <span class="brand__name">Verdanilo</span>
      </div>
      <p class="brand__tagline">Controlled Environment Agriculture</p>
    </div>

    <div class="divider"></div>

    <div class="contact">
      <h1 class="contact__name">MARCUS TRELL</h1>
      <p class="contact__role">Project Manager</p>
      <ul class="contact__list">
        <li class="contact__item">
          <svg class="contact__icon" viewBox="0 0 28 22" aria-hidden="true">
            <path d="M2 8 Q14 0 26 8 L26 10 L20 10 L19 7 Q14 5 9 7 L8 10 L2 10 Z" fill="var(--brand-green)"/>
            <path d="M6 12 H22 L24 21 H4 Z" fill="var(--brand-green)"/>
            <circle cx="14" cy="16" r="3" fill="#fff"/>
          </svg>
          (555) 304-2698
        </li>
        <li class="contact__item">
          <svg class="contact__icon" viewBox="0 0 28 22" aria-hidden="true">
            <rect x="3" y="3" width="22" height="16" fill="var(--brand-green)"/>
            <path d="M3 3 L14 12 L25 3 M3 19 L11 10 M25 19 L17 10" stroke="#fff" stroke-width="1.6" fill="none"/>
          </svg>
          Marc@verdanilo.com
        </li>
        <li class="contact__item">
          <svg class="contact__icon" viewBox="0 0 28 22" aria-hidden="true">
            <circle cx="14" cy="11" r="10" fill="var(--brand-green)"/>
            <path d="M4 11 H24 M14 1 V21 M14 1 Q7 11 14 21 M14 1 Q21 11 14 21" stroke="#fff" stroke-width="1.4" fill="none"/>
          </svg>
          www.verdanilo.com
        </li>
      </ul>
      <p class="contact__address">4200 W. Lindell Ave, Suite 310,<br>Fairhaven, CO 80199</p>
    </div>
  </section>

  <section class="card card--back">
    <div class="back-brand">
      <span class="back-brand__dot"></span>
      <span class="back-brand__name">Verdanilo</span>
    </div>
  </section>
</body>
</html>
```